Harbor Crest Motors

I’m looking for artwork that can go on the back of my vehicles that I sell. It’s going to be a magnet on the back of the vehicle. On the magnet it needs to state - I am for sale!
Please visit - harborcrestmotors.com

And in all caps - WE BEAT ANY PRICE!

Logo attached

Target Market(s)

Car sales

Industry/Entity Type

Car sales

```html
<!DOCTYPE html>
<html lang="en">
<head>
<meta charset="utf-8">
<title>Harbor Crest Motors – For Sale Magnet</title>
<link rel="stylesheet" href="https://fonts.googleapis.com/css2?family=Poppins:ital,wght@0,400;0,800;1,800;1,900&display=swap">
<style>
  :root {
    --stage: #ededed;
    --paper: #ffffff;
    --sale-red: #ec1c24;
    --ink: #231f20;
    --white: #ffffff;
  }
  html, body {
    margin: 0;
    padding: 0;
    width: 910px;
    height: 1200px;
    overflow: hidden;
    background: var(--stage);
    font-family: "Poppins", sans-serif;
  }
  .magnet {
    position: absolute;
    left: 25px;
    top: 313px;
    width: 860px;
    height: 573px;
    background: var(--paper);
    overflow: hidden;
    box-shadow: 0 6px 18px rgba(0,0,0,0.18);
  }
  .sun-art {
    position: absolute;
    inset: 0;
  }
  .headline-top,
  .headline-sale,
  .price-promise,
  .dealer-name {
    position: absolute;
    margin: 0;
    white-space: nowrap;
    line-height: 1;
  }
  .headline-top {
    left: 222px;
    top: 70px;
    font-size: 88px;
    font-weight: 900;
    font-style: italic;
    letter-spacing: -3px;
    color: var(--ink);
  }
  .headline-sale {
    left: 222px;
    top: 133px;
    font-size: 136px;
    font-weight: 900;
    font-style: italic;
    letter-spacing: -4px;
    color: var(--white);
  }
  .visit-bar {
    position: absolute;
    left: 233px;
    top: 260px;
    width: 367px;
    height: 29px;
    display: flex;
    font-size: 17px;
    font-weight: 400;
    color: var(--white);
  }
  .visit-label {
    width: 120px;
    border: 2px solid var(--ink);
    box-sizing: border-box;
    display: flex;
    align-items: center;
    padding-left: 10px;
  }
  .visit-url {
    flex: 1;
    background: var(--ink);
    display: flex;
    align-items: center;
    justify-content: center;
  }
  .price-promise {
    left: 232px;
    top: 302px;
    font-size: 35px;
    font-weight: 800;
    font-style: italic;
    letter-spacing: -0.5px;
    color: var(--white);
  }
  .dealer-mark {
    position: absolute;
    left: 268px;
    top: 362px;
    display: flex;
    align-items: center;
    gap: 10px;
  }
  .dealer-dot {
    width: 28px;
    height: 28px;
    border-radius: 50%;
    background: var(--white);
  }
  .dealer-name {
    position: static;
    font-size: 27px;
    font-weight: 800;
    color: var(--ink);
  }
  .car-illustration {
    position: absolute;
    left: 244px;
    top: 460px;
    width: 406px;
    height: 113px;
    background: linear-gradient(180deg, #c0161c 0%, #8d1216 100%);
    border-radius: 40px 60px 0 0;
  }
</style>
</head>
<body>
  <section class="magnet">
    <svg class="sun-art" width="860" height="573" viewBox="0 0 860 573" aria-hidden="true">
      <circle cx="430" cy="253" r="330" fill="var(--sale-red)"/>
      <g stroke="var(--white)" stroke-width="3" stroke-linecap="round">
        <line x1="374" y1="20" x2="653" y2="20"/>
        <line x1="162" y1="54" x2="240" y2="54"/>
        <line x1="589" y1="99" x2="723" y2="99"/>
        <line x1="585" y1="253" x2="760" y2="253"/>
        <line x1="102" y1="293" x2="171" y2="293"/>
        <line x1="132" y1="395" x2="266" y2="395"/>
        <line x1="499" y1="451" x2="689" y2="451"/>
      </g>
    </svg>

    <h1 class="headline-top">I AM FOR</h1>
    <h2 class="headline-sale">SALE!</h2>

    <div class="visit-bar">
      <span class="visit-label">Please visit</span>
      <span class="visit-url">harborcrestmotors.com</span>
    </div>

    <p class="price-promise">WE BEAT ANY PRICE!</p>

    <div class="dealer-mark">
      <span class="dealer-dot"></span>
      <span class="dealer-name">Harbor Crest Motors</span>
    </div>

    <div class="car-illustration" role="img" aria-label="Line drawing of a sports car in dark ink over the red circle"></div>
  </section>
</body>
</html>
```